依頼詳細
【店舗名】
コインランドリー緑坂店
【店舗特徴】
・2023年8月オープンの為、最新機器と清潔感のある店内
・現金、キャッシュレス決済、ICカード決済などの豊富な決済方法
・ICカードにチャージで10%還元
記載項目
記載必須項目
・会社ロゴ
・店舗住所
・お問合せ先
・コース金額
サイズ
A4
ページ数
両面
希望イメージ
シンプル 複雑
単色 カラフル
暗い 明るい
日常 高級
遊び心 厳粛
未来的 伝統的
女性的 男性的
希望する色
赤系、青系、水色系、特に指定はございません。
納品ファイル
• イラストレーター形式 (.ai)
補足説明
必須記載項目を記載していただければ、制作者様の自由にデザインしていただいて構いません。
※添付のコース表はキャンペーン非適用時の値段になりますので、キャンペーン中は全て添付コース表の半額になります。
一部訂正がありましたので追記させていただきます。

【内容】
■誤 ICカード

■正 ランドリーカード

よろしくお願い致します。
■ 選んだ理由

新年のキャンペーンで半額であることが分かりやすく、人の写真もあり目を引く内容だった。
カラーもきらびやかで綺麗にまとめていただいていた。

■ 提案者全員のお礼・コメント

チラシのコンペに御参加いただきまして誠にありがとうございます。
我々の社内検討だけでは思いつかないような斬新なアイデアも多く感謝しております。
今後ともよろしくお願いい達します。

```html
<!DOCTYPE html>
<html lang="ja">
<head>
<meta charset="UTF-8">
<title>初売りキャンペーン｜コインランドリー緑坂店</title>
<link href="https://fonts.googleapis.com/css2?family=Dela+Gothic+One&family=Noto+Sans+JP:wght@500;700;900&display=swap" rel="stylesheet">
<style>
:root{
  --red:#d7141d;
  --red-deep:#a80c12;
  --gold:#e9b730;
  --cream:#fffaf0;
  --green:#1f8a3c;
  --ink:#222;
  --grey:#777;
  --yellow:#ffe23a;
  --navy:#1d2433;
  --line:#e3d6c2;
}
*{box-sizing:border-box;margin:0;padding:0}
html,body{width:846px;height:1200px;overflow:hidden}
body{font-family:"Noto Sans JP",sans-serif;color:var(--ink);background:#fff}
.flyer{position:relative;width:846px;height:1200px;overflow:hidden;
  background:radial-gradient(circle at 50% 30%,#e42a2f 0%,var(--red) 45%,var(--red-deep) 100%)}
.title{position:absolute;top:8px;left:0;width:100%;text-align:center;
  font-family:"Dela Gothic One",sans-serif;font-size:58px;color:#fff;letter-spacing:2px;
  text-shadow:0 3px 0 var(--red-deep)}
.title .yr{color:var(--yellow)}

/* offer box */
.offer{position:absolute;top:92px;left:24px;width:798px;height:212px;background:var(--cream);
  border:4px solid var(--gold);border-radius:10px}
.card-visual{position:absolute;top:16px;left:24px;width:200px;height:120px;border-radius:10px;
  background:linear-gradient(135deg,#2a2a2a,#000)}
.card-note{position:absolute;top:144px;left:20px;width:210px;font-size:11px;color:var(--grey);text-align:center}
.mascot{position:absolute;top:158px;left:6px;width:82px;height:82px;border-radius:50%;
  background:linear-gradient(135deg,#6fb6e0,#2f78b8)}
.offer-lead{position:absolute;top:12px;left:250px;font-size:24px;font-weight:900;color:var(--ink)}
.offer-big{position:absolute;top:40px;left:248px;font-family:"Dela Gothic One",sans-serif;
  font-size:92px;line-height:1;color:var(--red)}
.offer-big small{font-size:68px}
.offer-sub{position:absolute;top:136px;left:250px;font-size:18px;font-weight:700}
.offer-bonus{position:absolute;top:163px;left:250px;font-size:22px;font-weight:900;display:flex;align-items:center;gap:6px;line-height:1.3}
.offer-bonus .tag{background:var(--red);color:#fff;font-size:16px;padding:1px 8px;border-radius:3px}
.offer-bonus em{font-style:normal;color:var(--red);font-size:26px}

/* price tables */
.menus{position:absolute;top:312px;left:24px;width:798px;height:478px;display:flex;gap:10px}
.menu{flex:1;background:#fff;border-radius:8px;padding:8px 10px}
.menu-head{background:var(--green);color:#fff;font-weight:900;font-size:16px;text-align:center;
  padding:3px 0;border-radius:4px;margin-bottom:4px}
.menu-head.shoes{background:var(--red);margin-top:6px}
.machine{font-size:13px;font-weight:900;color:var(--red);margin-top:5px;border-bottom:2px solid var(--red);padding-bottom:1px}
.machine span{font-size:10px;color:var(--grey);font-weight:500}
.row{display:grid;grid-template-columns:92px 64px 1fr 16px 66px;align-items:center;
  height:26px;border-bottom:1px dashed var(--line);font-size:14px;font-weight:700}
.row .spec{font-size:11px;color:var(--grey);font-weight:500}
.row .was{font-size:12px;color:var(--grey);text-decoration:line-through;text-align:right}
.row .arrow{color:var(--red);font-size:11px;text-align:center}
.row .now{color:var(--red);font-weight:900;font-size:18px;text-align:right}
.row .now small{font-size:11px}

/* point day */
.points{position:absolute;top:800px;left:24px;width:798px;height:146px;display:flex;gap:10px}
.point-day{flex:1.7;background:var(--yellow);border-radius:8px;position:relative;overflow:hidden}
.point-day .monthly{position:absolute;top:12px;left:12px;width:40px;height:96px;background:var(--red);color:#fff;
  font-weight:900;font-size:22px;line-height:1.1;border-radius:4px;display:flex;align-items:center;justify-content:center;
  writing-mode:vertical-rl;letter-spacing:4px}
.point-day .headline{position:absolute;top:6px;left:64px;font-family:"Dela Gothic One",sans-serif;color:var(--red);line-height:1.2}
.point-day .headline .l1{display:block;font-size:36px}
.point-day .headline .l2{display:block;font-size:34px}
.point-day .headline b{font-size:48px;font-weight:400}
.days{position:absolute;top:50px;right:14px;display:flex;gap:6px}
.day{width:62px;height:62px;border-radius:50%;background:var(--red);color:#fff;font-family:"Dela Gothic One",sans-serif;
  font-size:26px;display:flex;align-items:center;justify-content:center}
.day small{font-size:13px}
.period{position:absolute;bottom:10px;right:16px;font-size:12px;font-weight:700}
.charge-box{flex:1;background:var(--navy);color:#fff;border-radius:8px;padding:14px;font-size:14px;font-weight:700;line-height:1.6}
.charge-box strong{color:var(--yellow);font-size:17px;display:block}

/* features */
.features{position:absolute;top:956px;left:24px;width:798px;height:198px;background:#fff;border-radius:8px}
.staff-photo{position:absolute;top:10px;left:10px;width:150px;height:178px;border-radius:6px;
  background:linear-gradient(180deg,#f3d9c6,#9ec5de)}
.feature-label{position:absolute;top:120px;left:10px;width:230px;background:var(--red);color:#fff;border-radius:6px;padding:6px 10px}
.feature-label small{display:block;font-size:12px;font-weight:700}
.feature-label b{font-size:28px;font-weight:900}
.feature-list{position:absolute;top:18px;left:260px;list-style:none;font-size:17px;font-weight:700;line-height:2}
.feature-list li{display:flex;align-items:center;gap:8px}
.feature-list svg{flex:none}

.footer{position:absolute;bottom:0;left:0;width:100%;height:42px;background:var(--red-deep);color:#fff;
  display:flex;align-items:center;justify-content:center;gap:20px;font-weight:900;font-size:17px}
.footer .tel{font-size:22px;color:var(--yellow)}
</style>
</head>
<body>
<div class="flyer">
  <h1 class="title"><span class="yr">24</span>初売りキャンペーン</h1>

  <section class="offer">
    <div class="card-visual" role="img" aria-label="ランドリーカードのイメージ"></div>
    <p class="card-note">ランドリーカードは精算機で購入できます</p>
    <div class="mascot" role="img" aria-label="干支のキャラクターイラスト"></div>
    <p class="offer-lead">ランドリーカード決済で全コース</p>
    <p class="offer-big">50<small>%</small>OFF</p>
    <p class="offer-sub">ランドリーカードは、店内精算機でカンタン購入。</p>
    <p class="offer-bonus"><span class="tag">さらに</span>カードにチャージで<em>10%還元</em></p>
  </section>

  <section class="menus">
    <div class="menu">
      <div class="menu-head">洗濯から乾燥までノンストップ</div>
      <div class="machine">ドラム式全自動洗濯乾燥機 <span>(洗濯17kg／乾燥10kg)</span></div>
      <div class="row"><span>洗濯</span><span class="spec">17kg</span><span class="was">1,000円</span><span class="arrow">▶</span><span class="now">500<small>円</small></span></div>
      <div class="row"><span>洗濯乾燥</span><span class="spec">60分</span><span class="was">1,200円</span><span class="arrow">▶</span><span class="now">600<small>円</small></span></div>
      <div class="row"><span>抗菌・消毒</span><span class="spec">60分</span><span class="was">1,300円</span><span class="arrow">▶</span><span class="now">650<small>円</small></span></div>
      <div class="machine">ドラム式全自動洗濯乾燥機 <span>(洗濯27kg／乾燥15kg)</span></div>
      <div class="row"><span>洗濯</span><span class="spec">27kg</span><span class="was">1,300円</span><span class="arrow">▶</span><span class="now">650<small>円</small></span></div>
      <div class="row"><span>洗濯乾燥</span><span class="spec">70分</span><span class="was">1,700円</span><span class="arrow">▶</span><span class="now">850<small>円</small></span></div>
      <div class="row"><span>抗菌・消毒</span><span class="spec">70分</span><span class="was">1,800円</span><span class="arrow">▶</span><span class="now">900<small>円</small></span></div>
      <div class="row"><span>敷布団洗濯</span><span class="spec">80分</span><span class="was">2,000円</span><span class="arrow">▶</span><span class="now">1,000<small>円</small></span></div>
      <div class="row"><span>羽毛ふとん</span><span class="spec">80分</span><span class="was">2,000円</span><span class="arrow">▶</span><span class="now">1,000<small>円</small></span></div>
      <div class="machine">ドラム式全自動洗濯乾燥機 <span>(洗濯22kg／乾燥12kg)</span></div>
      <div class="row"><span>洗濯乾燥</span><span class="spec">65分</span><span class="was">1,500円</span><span class="arrow">▶</span><span class="now">750<small>円</small></span></div>
      <div class="row"><span>抗菌・消毒</span><span class="spec">65分</span><span class="was">1,600円</span><span class="arrow">▶</span><span class="now">800<small>円</small></span></div>
      <div class="row"><span>羽毛ふとん</span><span class="spec">75分</span><span class="was">1,800円</span><span class="arrow">▶</span><span class="now">900<small>円</small></span></div>
      <div class="row"><span>掛け布団</span><span class="spec">75分</span><span class="was">1,800円</span><span class="arrow">▶</span><span class="now">900<small>円</small></span></div>
    </div>

    <div class="menu">
      <div class="menu-head">ガス乾燥でふんわり乾燥</div>
      <div class="machine">ガス乾燥機 <span>(25kg)</span></div>
      <div class="row"><span>乾燥</span><span class="spec">25kg 10分</span><span class="was">100円</span><span class="arrow">▶</span><span class="now">50<small>円</small></span></div>
      <div class="row"><span>乾燥</span><span class="spec">25kg 8分</span><span class="was">100円</span><span class="arrow">▶</span><span class="now">50<small>円</small></span></div>
      <div class="machine">ガス乾燥機 <span>(ふとん対応 25kg)</span></div>
      <div class="row"><span>乾燥</span><span class="spec">25kg 8分</span><span class="was">100円</span><span class="arrow">▶</span><span class="now">50<small>円</small></span></div>
      <div class="machine">ガス乾燥機 <span>(14kg)</span></div>
      <div class="row"><span>乾燥</span><span class="spec">14kg 10分</span><span class="was">100円</span><span class="arrow">▶</span><span class="now">50<small>円</small></span></div>
      <div class="row"><span>乾燥</span><span class="spec">14kg 12分</span><span class="was">100円</span><span class="arrow">▶</span><span class="now">50<small>円</small></span></div>
      <div class="machine">シングル乾燥機</div>
      <div class="row"><span>乾燥</span><span class="spec">12分</span><span class="was">100円</span><span class="arrow">▶</span><span class="now">50<small>円</small></span></div>
      <div class="menu-head shoes">子供の運動靴から大人のスニーカーまで</div>
      <div class="machine">スニーカーウォッシャー <span>(大人2足)</span></div>
      <div class="row"><span>洗濯</span><span class="spec">20分</span><span class="was">200円</span><span class="arrow">▶</span><span class="now">100<small>円</small></span></div>
      <div class="machine">スニーカードライヤー <span>(大人2足)</span></div>
      <div class="row"><span>乾燥</span><span class="spec">20分</span><span class="was">100円</span><span class="arrow">▶</span><span class="now">50<small>円</small></span></div>
    </div>
  </section>

  <section class="points">
    <div class="point-day">
      <span class="monthly">毎月</span>
      <p class="headline"><span class="l1"><b>5</b>のつく日</span><span class="l2">ポイント<b>2</b>倍</span></p>
      <div class="days">
        <div class="day">5<small>日</small></div>
        <div class="day">15<small>日</small></div>
        <div class="day">25<small>日</small></div>
      </div>
      <p class="period">※期間限定2024年2月末まで</p>
    </div>
    <div class="charge-box">
      <strong>ランドリーカードにチャージして</strong>
      ポイントをゲット！<br>
      チャージ額に応じてお得なポイントがたまります。
    </div>
  </section>

  <section class="features">
    <div class="staff-photo" role="img" aria-label="店内の洗濯機の前に立つ利用者の写真"></div>
    <div class="feature-label"><small>おすすめの機能説明</small><b>ここがポイント</b></div>
    <ul class="feature-list">
      <li><svg width="18" height="18" viewBox="0 0 18 18"><circle cx="9" cy="9" r="9" fill="#d7141d"/><path d="M4.5 9.5l3 3 6-6" stroke="#fff" stroke-width="2.2" fill="none"/></svg>最新の設備で清潔感のある店内</li>
      <li><svg width="18" height="18" viewBox="0 0 18 18"><circle cx="9" cy="9" r="9" fill="#d7141d"/><path d="M4.5 9.5l3 3 6-6" stroke="#fff" stroke-width="2.2" fill="none"/></svg>現金・キャッシュレス・ランドリーカード決済対応</li>
      <li><svg width="18" height="18" viewBox="0 0 18 18"><circle cx="9" cy="9" r="9" fill="#d7141d"/><path d="M4.5 9.5l3 3 6-6" stroke="#fff" stroke-width="2.2" fill="none"/></svg>ガス乾燥機でふんわり仕上がり</li>
      <li><svg width="18" height="18" viewBox="0 0 18 18"><circle cx="9" cy="9" r="9" fill="#d7141d"/><path d="M4.5 9.5l3 3 6-6" stroke="#fff" stroke-width="2.2" fill="none"/></svg>ふとん・スニーカーもまとめて洗える</li>
    </ul>
  </section>

  <footer class="footer">
    <span>コインランドリー緑坂店</span>
    <span>お問い合わせ <span class="tel">0120-000-123</span></span>
  </footer>
</div>
</body>
</html>
```